KLO Personal sucht Visitenkarten u. Briefpapier Design
It was a very good project! Very quick and perfect design!
Zielgruppe
Wir sind ein Liechtensteiner Personaldienstleisungsunternehmen welches sowohl in der klassischen Personalvermittlung als auch in der temporären Personalbereitstellung tätig ist. Unsere Branchen reichen von Baugewerbe, Handwerk, Gastro- und Hotelerie bis hin zu Produktion und Gesundheitswesen.
Achtung:
Habe gerade die files vom neuen Logo hochgeladen!!!
Aufgabenstellung
Visitienkarten designen.
Briefpapier Vorlagenerstellung.
Schlichtes Visitenkartendesign Business auf der nicht zuviele Informationen sind (das Wichtigste)
Vorderseite:
Logo (wird vor Abschluss noch in besserer Qualität hochgeladen)
Firmenname
Anschrift
Name
Funktion
Telefon
Fax
E-Mail
Homepage
Rückseite:
Kann Kreativ gestaltet werden, farblich (blau, gelb, schwarz, weiss), nach Möglichkeit keinen weissen Hintergrund.
!!Bitte keine Vorschläge mit dem Fotoscanner ... da! Danke.
Wir freuen uns auch auf kreative Vorschläge, welche etwas vom Briefing abweichen.
KLO - Team

```html
<!DOCTYPE html>
<html lang="de">
<head>
<meta charset="utf-8">
<title>KLO Personal – Visitenkarte</title>
<link rel="stylesheet" href="https://fonts.googleapis.com/css2?family=Source+Sans+3:wght@400;600;700&display=swap">
<style>
  :root {
    --page-bg: #e6e8ec;
    --card-white: #f4f4f5;
    --card-grey: #e2e2e4;
    --brand-blue: #1a5bb5;
    --brand-navy: #0d2f7a;
    --deep-blue: #071c5c;
    --light-blue: #5fa8e8;
    --text-dark: #1c1c1c;
    --white: #ffffff;
  }
  * { box-sizing: border-box; margin: 0; padding: 0; }
  html, body {
    width: 1200px;
    height: 760px;
    overflow: hidden;
    background: var(--page-bg);
    font-family: "Source Sans 3", "Myriad Pro", Arial, sans-serif;
  }
  .canvas {
    position: relative;
    width: 1200px;
    height: 760px;
  }
  .card {
    position: absolute;
    top: 230px;
    width: 520px;
    height: 300px;
    overflow: hidden;
    box-shadow: 0 10px 30px rgba(0, 0, 0, 0.18);
  }
  .card--front {
    left: 50px;
    background: radial-gradient(ellipse at 10% 40%, var(--card-grey) 0%, var(--card-white) 60%);
  }
  .card--back {
    left: 630px;
  }
  .front-band {
    position: absolute;
    left: 0;
    right: 0;
    bottom: 0;
    height: 10px;
    background: var(--brand-blue);
  }
  .wordmark {
    position: absolute;
    display: flex;
    align-items: center;
    gap: 8px;
    font-weight: 700;
    line-height: 1;
  }
  .wordmark__dot {
    border-radius: 50%;
    flex: none;
  }
  .card--front .wordmark {
    left: 34px;
    top: 36px;
    font-size: 34px;
    color: var(--brand-navy);
  }
  .card--front .wordmark__dot {
    width: 16px;
    height: 16px;
    background: var(--brand-blue);
  }
  .holder {
    position: absolute;
    left: 220px;
    top: 150px;
    padding-left: 14px;
    border-left: 1.5px solid var(--brand-blue);
    height: 110px;
  }
  .holder__name {
    font-size: 17px;
    font-weight: 700;
    color: var(--brand-blue);
    margin-bottom: 22px;
  }
  .holder__company {
    font-size: 12.5px;
    font-weight: 700;
    color: var(--brand-blue);
    line-height: 1.25;
  }
  .holder__address {
    font-size: 12px;
    color: var(--text-dark);
    line-height: 1.3;
    font-style: normal;
  }
  .contact {
    position: absolute;
    left: 375px;
    top: 188px;
    display: grid;
    grid-template-columns: auto auto;
    column-gap: 8px;
    row-gap: 2px;
    font-size: 12px;
  }
  .contact dt { color: var(--brand-blue); }
  .contact dd { color: var(--text-dark); text-align: right; }
  .back-pattern {
    position: absolute;
    inset: 0;
    background:
      radial-gradient(ellipse at 85% 70%, var(--light-blue) 0%, rgba(95, 168, 232, 0) 55%),
      linear-gradient(135deg, var(--deep-blue) 0%, var(--brand-navy) 50%, var(--brand-blue) 100%);
  }
  .card--back .wordmark {
    left: 40px;
    bottom: 32px;
    font-size: 24px;
    color: var(--white);
  }
  .card--back .wordmark__dot {
    width: 11px;
    height: 11px;
    background: var(--white);
  }
</style>
</head>
<body>
<main class="canvas">
  <section class="card card--front" aria-label="Visitenkarte Vorderseite">
    <div class="wordmark">
      <span class="wordmark__dot"></span>
      <span class="wordmark__name">KLO Personal</span>
    </div>
    <div class="holder">
      <p class="holder__name">Jonas Beispiel</p>
      <p class="holder__company">KLO Personal</p>
      <address class="holder__address">
        Talstrasse 12<br>
        9490 Musterdorf<br>
        Liechtenstein
      </address>
    </div>
    <dl class="contact">
      <dt>E-Mail:</dt><dd>office@klo.li</dd>
      <dt>Fax:</dt><dd>+423 555 20 01</dd>
      <dt>Tel:</dt><dd>+423 555 20 00</dd>
      <dt>Web:</dt><dd>www.klo.li</dd>
    </dl>
    <div class="front-band"></div>
  </section>

  <section class="card card--back" aria-label="Visitenkarte Rückseite">
    <div class="back-pattern" role="img" aria-label="Blaues Flächenmuster aus sich wiederholenden Figuren, zur rechten unteren Ecke hin heller"></div>
    <div class="wordmark">
      <span class="wordmark__dot"></span>
      <span class="wordmark__name">KLO Personal</span>
    </div>
  </section>
</main>
</body>
</html>
```